Looking for a high-end business card design for a construction company

We are looking to update our business card design. We are a post-frame construction company that builds custom buildings, commercial spaces, homes, and anything else. We have multiple people working here so we would need something we can easily customize the information for the specific person. We need a name, website, cell phone, office phone as well as social icons. Our colors are black, white, and grey/silver so I would love a black background or something that is more striking than just a traditional white business card. Looking for something that is very professional with a high-end look/feel. I have attached our logos, they can be silver, white, grey, or black.
Industry/Entity Type
Construction
Contact Information for Business Card
Business logo, Name, Cell phone, Office phone, website, social Icons
Colors
Designer to choose only greyscale colors for use in the design.
Look and feel

```html
<!DOCTYPE html>
<html lang="en">
<head>
<meta charset="utf-8">
<title>Harwell Builders, Inc. — Business Card</title>
<link href="https://fonts.googleapis.com/css2?family=Montserrat:wght@400;700&display=swap" rel="stylesheet">
<style>
  :root {
    --stage: #222222;
    --card: #0f0f0f;
    --card-edge: #1a1a1a;
    --ink: #f2f2f2;
    --ink-soft: #cfcfcf;
    --mark: #e6e6e6;
  }
  * { box-sizing: border-box; margin: 0; padding: 0; }
  html, body {
    width: 1200px; height: 939px; overflow: hidden;
    background: var(--stage);
    font-family: "Montserrat", sans-serif;
  }
  .canvas { position: relative; width: 1200px; height: 939px; }
  .card {
    position: absolute;
    width: 462px; height: 264px;
    background: var(--card);
    border: 1px solid var(--card-edge);
    border-radius: 3px;
  }
  .card--front { left: 110px; top: 150px; }
  .card--back { left: 628px; top: 525px; }

  .brand {
    position: absolute; inset: 0;
    display: flex; align-items: center; justify-content: center; gap: 14px;
  }
  .brand__dot {
    width: 26px; height: 26px; border-radius: 50%;
    background: var(--mark);
  }
  .brand__name {
    color: var(--mark);
    font-weight: 700; font-size: 22px; letter-spacing: 3px;
    text-transform: uppercase;
  }

  .contact {
    position: absolute; left: 34px; bottom: 34px;
    color: var(--ink);
  }
  .contact__name {
    font-weight: 700; font-size: 17px; letter-spacing: 1px;
    text-transform: uppercase; margin-bottom: 12px;
  }
  .contact__list { list-style: none; }
  .contact__item {
    display: flex; align-items: center; gap: 8px;
    font-size: 12px; line-height: 19px; color: var(--ink-soft);
  }
  .contact__icon { width: 10px; height: 10px; flex: none; }
</style>
</head>
<body>
<main class="canvas">
  <section class="card card--front" aria-label="Card front">
    <div class="brand">
      <span class="brand__dot"></span>
      <span class="brand__name">Harwell Builders, Inc.</span>
    </div>
  </section>

  <section class="card card--back" aria-label="Card back">
    <div class="contact">
      <p class="contact__name">Daniel Reyes</p>
      <ul class="contact__list">
        <li class="contact__item">
          <svg class="contact__icon" viewBox="0 0 10 10"><path d="M2 0.5 L4 2.5 L3 3.7 Q4.2 5.8 6.3 7 L7.5 6 L9.5 8 L8 9.5 Q3 9 0.5 2 Z" fill="#cfcfcf"/></svg>
          555-214-0387
        </li>
        <li class="contact__item">
          <svg class="contact__icon" viewBox="0 0 10 10"><rect x="2" y="0.5" width="6" height="9" rx="1" fill="none" stroke="#cfcfcf" stroke-width="1.2"/></svg>
          555-318-2046
        </li>
        <li class="contact__item">
          <svg class="contact__icon" viewBox="0 0 10 10"><rect x="0.5" y="2" width="9" height="6.5" fill="#cfcfcf"/><path d="M0.5 2 L5 5.5 L9.5 2" fill="none" stroke="#0f0f0f" stroke-width="1"/></svg>
          info@harwellbuilders.com
        </li>
        <li class="contact__item">
          <svg class="contact__icon" viewBox="0 0 10 10"><circle cx="5" cy="5" r="4.5" fill="#cfcfcf"/><path d="M3 5 H7 M5 3 L7 5 L5 7" fill="none" stroke="#0f0f0f" stroke-width="1"/></svg>
          www.harwellbuilders.com
        </li>
      </ul>
    </div>
  </section>
</main>
</body>
</html>
```